New Website Design for NAPTO.org

We are looking for a new website design for NAPTO.org. NAPTO is a non profit home inspector association based in California. Home Inspectors are people that come out and look at a house before it's purchased to let the buyer know of any defects that may exist.
Our site is based on Joomla so if you'll be able to make a Joomla 3 template as well, please let us know (not required, but a bonus).
We would like to see designs that incorporate royal blue, white and chrome into the site as that's our main business colors.
We would like a place for rotating banners though they don't need to be the same size as the current site.
We would like navigation to be easier to manage with menus only across the top (via drop down menus) where we are going to sort out the items currently on the side. Possibly the front page could have a graphic link to separate portals for Realtors, Home Buyers and Inspectors, but that's just one option.
We would like a good mobile design or something that will scale easily to mobile.
The Find an Inspector feature is important and should stand out. The ASK NAPTOr site
Current home page feels a bit busy. Would like to simplify a bit.
Non Profit

```html
<!DOCTYPE html>
<html lang="en">
<head>
<meta charset="utf-8">
<title>NAPTO — Home</title>
<link href="https://fonts.googleapis.com/css2?family=Ubuntu:wght@400;500;700&family=Open+Sans:wght@400;600&display=swap" rel="stylesheet">
<style>
:root{
  --royal:#1d3f9b;
  --royal-dark:#12307f;
  --royal-band:#2c4ea8;
  --ink:#333;
  --muted:#8b8b8b;
  --line:#dcdcdc;
  --panel:#f3f3f3;
  --footer:#2b2b2b;
  --footer-text:#cfcfcf;
  --white:#fff;
}
*{margin:0;padding:0;box-sizing:border-box}
html,body{width:969px;height:1200px;overflow:hidden}
body{position:relative;font-family:"Open Sans",Arial,sans-serif;color:var(--ink);background:#c9c9c9}
.backdrop{position:absolute;left:0;top:0;width:969px;height:480px;
  background:linear-gradient(180deg,#7fa6d6 0%,#c78a45 30%,#b27036 55%,#c8c8c8 100%)}
.topline{position:absolute;left:0;top:0;width:969px;height:3px;background:var(--royal)}
.page{position:absolute;left:120px;top:3px;width:738px;height:1197px;background:var(--white)}
.abs{position:absolute}

/* header */
.brand{left:36px;top:22px;display:flex;align-items:center;gap:10px}
.brand-dot{width:58px;height:58px;border-radius:50%;background:var(--royal)}
.brand-name{font-family:"Ubuntu",Arial,sans-serif;font-weight:700;font-size:30px;color:var(--royal)}
.search{left:412px;top:39px;width:157px;height:23px;border:1px solid #ccc;border-radius:3px;
  font-size:10px;color:#888;padding:5px 8px;letter-spacing:.5px}
.search svg{position:absolute;right:6px;top:4px}
.search::after{content:"";position:absolute;right:24px;top:2px;width:1px;height:17px;background:#ddd}
.vsep{left:592px;top:17px;width:1px;height:60px;background:#ddd}
.contact{left:605px;top:18px;font-family:"Ubuntu",Arial,sans-serif;font-size:14px;line-height:17px;color:var(--royal)}
.contact a{color:var(--royal);text-decoration:underline;display:block;margin-top:2px}
.nav{left:198px;top:92px;width:520px;display:flex;align-items:center;justify-content:space-between;
  font-family:"Ubuntu",Arial,sans-serif;font-size:10.5px;color:#444;white-space:nowrap}
.nav .active{background:var(--royal);color:#fff;font-weight:700;padding:4px 7px;border-radius:2px}

/* hero */
.hero{left:28px;top:145px;width:678px;height:242px;overflow:hidden}
.hero-photo{position:absolute;left:150px;top:0;width:528px;height:242px;
  background:linear-gradient(160deg,#d6dde6 0%,#a7b1b9 35%,#8c8a80 60%,#6f8a4e 100%)}
.hero-panel{position:absolute;left:0;top:0;width:200px;height:242px;background:var(--royal);
  clip-path:polygon(0 0,100% 0,88% 100%,0 100%)}
.hero-menu{position:absolute;left:0;top:0;width:180px}
.hero-item{height:58px;display:flex;align-items:center;gap:12px;padding-left:18px;
  border-bottom:1px solid rgba(255,255,255,.08);box-shadow:0 1px 0 rgba(0,0,0,.15);
  font-family:"Ubuntu",Arial,sans-serif;font-size:12.5px;line-height:13px;color:#fff;white-space:nowrap}
.hero-icon{width:33px;height:33px;border-radius:50%;background:#fff;flex:none;display:flex;align-items:center;justify-content:center}
.hero-caption{position:absolute;left:188px;top:187px;width:490px;height:55px;background:rgba(20,20,20,.88);
  padding:7px 0 0 16px;color:#fff}
.hero-caption h1{font-family:"Ubuntu",Arial,sans-serif;font-size:18px;font-weight:700;line-height:20px}
.hero-caption p{font-size:8.5px;line-height:10px;margin-top:3px;width:450px}

/* finder */
.finder{left:28px;top:387px;width:678px;height:69px;background:var(--panel);border:1px solid #e2e2e2}
.finder-title{left:20px;top:12px;display:flex;gap:6px;align-items:center;font-family:"Ubuntu",Arial,sans-serif;font-size:11px;font-weight:500;color:var(--royal)}
.select{left:26px;top:36px;width:180px;height:20px;border:1px solid #ddd;background:#eee;font-size:8.5px;color:#777;padding:4px 8px}
.select::after{content:"";position:absolute;right:10px;top:8px;border:4px solid transparent;border-top-color:#888}
.fsep{top:8px;width:1px;height:52px;background:#ddd}
.flabel{font-size:8px;color:#555;top:27px}
.finput{top:43px;width:96px;height:19px;border:1px solid #ddd;background:#eee;font-size:7.5px;color:#aaa;padding:4px 6px}
.fbutton{left:541px;top:25px;width:100px;height:30px;background:#151515;border-radius:3px;color:#fff;
  font-family:"Ubuntu",Arial,sans-serif;font-size:17px;text-align:center;line-height:30px}
.hr{left:4px;width:730px;height:1px;background:var(--line)}

/* features */
.card{top:504px;width:146px}
.card-img{height:60px;border-radius:3px 3px 0 0}
.card-label{height:24px;background:var(--royal-band);color:#fff;font-size:9px;padding:6px 7px;border-radius:0 0 3px 3px;white-space:nowrap}
.card p{font-size:8px;line-height:12.5px;color:var(--muted);padding:14px 7px 0}

/* gallery */
.sec-title{left:42px;top:679px;display:flex;align-items:center;gap:6px;font-family:"Ubuntu",Arial,sans-serif;font-size:11.5px;color:var(--royal);font-weight:500}
.sec-title i{width:11px;height:11px;background:var(--royal)}
.gallery{left:42px;top:698px;width:443px;height:147px;border:1px solid #ddd;overflow:hidden}
.gallery div{position:absolute}
.g-text{left:42px;top:863px;width:450px;font-size:8.5px;line-height:13px;color:#555}
.social{left:513px;top:696px;width:193px;height:64px;background:var(--royal);padding:8px 11px;color:#fff;box-shadow:0 6px 6px -4px rgba(0,0,0,.25)}
.social small{display:block;font-size:8px;color:#b8c6ea}
.social strong{font-family:"Ubuntu",Arial,sans-serif;font-size:22px;font-weight:700}
.social .like{position:absolute;right:11px;top:22px;width:46px;height:15px;background:#eef1f7;color:#444;font-size:7px;text-align:center;line-height:15px}
.about{left:513px;top:784px;width:193px;height:77px;border:1px solid #ddd;padding:11px 10px;box-shadow:0 5px 6px -4px rgba(0,0,0,.2)}
.about h3{font-family:"Ubuntu",Arial,sans-serif;font-weight:400;font-size:10px;line-height:13px;color:#333;width:118px}
.about a{position:absolute;left:13px;top:59px;font-size:8px;color:#333;text-decoration:underline}
.about .seal{position:absolute;right:10px;top:9px;width:56px;height:56px;border-radius:50%;background:linear-gradient(135deg,#eee,#aaa);border:2px solid #bbb}

/* footer */
.footer{left:0;top:905px;width:738px;height:292px;background:var(--footer);border-top:4px solid #555;color:var(--footer-text)}
.f-col{top:24px}
.f-col h4{font-family:"Ubuntu",Arial,sans-serif;font-size:11.5px;font-weight:500;color:#fff;letter-spacing:.3px;margin-bottom:20px}
.news{display:flex;gap:10px;margin-bottom:11px}
.news .thumb{width:40px;height:40px;flex:none}
.news div{width:150px}
.news b{display:block;font-family:"Ubuntu",Arial,sans-serif;font-weight:400;font-size:10.5px;color:#fff;margin:2px 0 3px}
.news span{display:block;font-size:7px;line-height:11px;color:#bbb}
.tweet{font-size:8px;line-height:14px;color:#bbb;width:145px}
.tweet em{font-style:normal;color:#fff}
.time{display:flex;align-items:center;gap:6px;font-size:8px;color:#fff;margin:12px 0 14px}
.tline{width:145px;height:1px;background:#444;margin-top:-6px}
.popular li{list-style:none;font-size:8.5px;color:#fff;margin-bottom:13px;padding-left:12px;position:relative;white-space:nowrap}
.popular li::before{content:"";position:absolute;left:0;top:3px;border:3px solid transparent;border-left:4px solid #fff}
.fg{display:grid;grid-template-columns:repeat(3,44px);gap:5px 4px}
.fg div{height:44px}
.footbar{left:0;top:252px;width:738px;height:40px;border-top:1px solid #1e1e1e;background:var(--footer);padding:14px 42px;font-size:8px;color:#ccc}
.footbar b{color:#fff;font-weight:400}
</style>
</head>
<body>
<div class="backdrop" role="img" aria-label="Timber house frames under construction against a blue sky"></div>
<div class="topline"></div>

<svg class="abs" style="left:128px;top:278px" width="12" height="28" viewBox="0 0 12 28"><path d="M10 2 2 14l8 12" fill="none" stroke="#888" stroke-width="2"/></svg>
<svg class="abs" style="left:836px;top:278px" width="12" height="28" viewBox="0 0 12 28"><path d="M2 2l8 12-8 12" fill="none" stroke="#888" stroke-width="2"/></svg>

<main class="page">
  <header>
    <div class="abs brand"><span class="brand-dot"></span><span class="brand-name">NAPTO</span></div>
    <div class="abs search">SEARCH
      <svg width="13" height="13" viewBox="0 0 13 13"><circle cx="5.5" cy="5.5" r="4" fill="none" stroke="#777" stroke-width="1.6"/><path d="M8.5 8.5 12 12" stroke="#777" stroke-width="1.8"/></svg>
    </div>
    <div class="abs vsep"></div>
    <div class="abs contact">(800) 555-0142<br>(916) 555-0187<a>info@napto.org</a></div>
    <nav class="abs nav">
      <span class="active">HOME</span><span>Find an Inspector</span><span>Home Buyers &amp; Sellers</span><span>Real Estate Agents</span><span>Inspectors</span><span>Ask NAPTO</span>
    </nav>
  </header>

  <section class="abs hero">
    <div class="hero-photo" role="img" aria-label="Two home inspectors examining a house window with clipboards"></div>
    <div class="hero-panel"></div>
    <div class="hero-menu">
      <div class="hero-item"><span class="hero-icon"><svg width="18" height="16" viewBox="0 0 18 16"><circle cx="6" cy="5" r="3.5" fill="#1d3f9b"/><path d="M0 15c0-4 3-6 6-6s6 2 6 6z" fill="#1d3f9b"/><circle cx="13" cy="4" r="3" fill="#1d3f9b"/></svg></span>INSPECTOR LOGIN</div>
      <div class="hero-item"><span class="hero-icon"><svg width="16" height="16" viewBox="0 0 16 16"><circle cx="8" cy="5" r="4" fill="#1d3f9b"/><path d="M1 16c0-5 3-7 7-7s7 2 7 7z" fill="#1d3f9b"/></svg></span>SEARCH FOR<br>INSPECTOR</div>
      <div class="hero-item"><span class="hero-icon"><svg width="17" height="16" viewBox="0 0 17 16"><rect x="1" y="3" width="13" height="12" rx="1" fill="none" stroke="#1d3f9b" stroke-width="1.8"/><path d="M1 6h13M4 1v4M11 1v4" stroke="#1d3f9b" stroke-width="1.8"/><circle cx="12" cy="11" r="4" fill="#1d3f9b"/></svg></span>UP COMMING<br>EVENTS</div>
      <div class="hero-item"><span class="hero-icon"><svg width="18" height="16" viewBox="0 0 18 16"><path d="M9 1 1 8h2v7h12V8h2z" fill="#1d3f9b"/><rect x="7" y="10" width="4" height="5" fill="#fff"/></svg></span>NAPTO NEW<br>CONSTRUCTION</div>
    </div>
    <div class="hero-caption">
      <h1>Welcome to NAPTO</h1>
      <p>The National Association of Property Testing Officers (NAPTO) is a voluntary, nonprofit public-benefit organization of real estate inspectors.</p>
    </div>
  </section>

  <section class="abs finder">
    <div class="abs finder-title"><svg width="20" height="18" viewBox="0 0 20 18"><rect x="3" y="2" width="12" height="14" fill="none" stroke="#1d3f9b" stroke-width="1.4"/><circle cx="8" cy="8" r="4" fill="none" stroke="#1d3f9b" stroke-width="1.6"/><path d="M5 11 1 15" stroke="#1d3f9b" stroke-width="2"/></svg>SEARCH FOR INSPECTOR</div>
    <div class="abs select">DISTANCE</div>
    <div class="abs fsep" style="left:237px"></div>
    <div class="abs flabel" style="left:270px">FROM:</div>
    <div class="abs flabel" style="left:380px">TO:</div>
    <div class="abs finput" style="left:268px">ANY</div>
    <div class="abs finput" style="left:378px">ANY</div>
    <div class="abs fsep" style="left:507px"></div>
    <div class="abs fbutton">SEARCH</div>
  </section>

  <div class="abs hr" style="top:475px"></div>

  <section>
    <article class="abs card" style="left:40px"><div class="card-img" role="img" aria-label="Forest path in green woodland" style="background:linear-gradient(#3f7a2a,#8fbf4a)"></div><div class="card-label">Path to Success Program</div><p>Duis aute irure dolor reprehenderit in voluptate velit esse cillum dolore eu fugiat nulla pariatur. Excepteur sint occaecat cupidatat.</p></article>
    <article class="abs card" style="left:213px"><div class="card-img" role="img" aria-label="Raised hand in front of a green chalkboard" style="background:linear-gradient(135deg,#2f8a5a,#7cc49a)"></div><div class="card-label">Educational Publications</div><p>Lorem ipsum dolor sit consectetur adipisicing elit amet sid do eiusmod tempor incididunt labore sint occaecat.</p></article>
    <article class="abs card" style="left:385px"><div class="card-img" role="img" aria-label="New construction specialist badge" style="background:#fff;border:1px solid #ddd;border-bottom:0"></div><div class="card-label">NAPTO New Construction</div><p>Duis aute irure dolor reprehenderit in voluptate velit esse cillum dolore eu fugiat nulla pariatur. Excepteur sint occaecat cupidatat.</p></article>
    <article class="abs card" style="left:558px"><div class="card-img" role="img" aria-label="Grey two-storey house facade" style="background:linear-gradient(#a9afb6,#5d646c)"></div><div class="card-label">NAPTO Press / Media Archives</div><p>Duis aute irure dolor reprehenderit in voluptate velit esse cillum dolore eu fugiat nulla pariatur. Excepteur sint occaecat cupidatat.</p></article>
  </section>

  <div class="abs hr" style="top:668px;left:40px;width:666px;background:#eee"></div>

  <section>
    <div class="abs sec-title"><i></i>GALLERY</div>
    <div class="abs gallery">
      <div role="img" aria-label="Woman reading in a bright lounge" style="left:3px;top:3px;width:130px;height:69px;background:linear-gradient(#eef0f2,#9aa3b3)"></div>
      <div role="img" aria-label="Glass roof structure" style="left:3px;top:75px;width:130px;height:67px;background:linear-gradient(135deg,#cfe4ec,#5f8ea0)"></div>
      <div role="img" aria-label="Man looking out over a city from an office window" style="left:136px;top:3px;width:165px;height:139px;background:linear-gradient(#d4dade,#5e6870)"></div>
      <div role="img" aria-label="Modern building facade with louvres" style="left:304px;top:3px;width:135px;height:66px;background:linear-gradient(90deg,#e4e4e4,#555,#e4e4e4)"></div>
      <div role="img" aria-label="Woman working on a laptop in a waiting area" style="left:304px;top:72px;width:135px;height:70px;background:linear-gradient(#f3f3f3,#8a8a8a)"></div>
    </div>
    <p class="abs g-text">El aluminio es un metal que se distingue de otros materiales por su propiedades tecnológicas. Su ligereza y su resistencia mecánica, lo hacen útil para múltiples y exigentes aplicaciones, ya que su densidad es un</p>

    <div class="abs social"><small>National Property Inspectors</small><strong>Circlebook</strong><span class="like">Like</span></div>
    <div class="abs about"><h3>National Association of Property Testing Officers</h3><span class="seal"></span><a>Read More</a></div>
  </section>

  <footer class="abs footer">
    <div class="abs f-col" style="left:41px">
      <h4>LATEST NEWS</h4>
      <div class="news"><span class="thumb" role="img" aria-label="Dinner event" style="background:linear-gradient(#6b2a1c,#c86b4a)"></span><div><b>Schedule</b><span>Lorem ipsum dolor amet laboris consectetur adipisicing elit,</span></div></div>
      <div class="news"><span class="thumb" role="img" aria-label="Conference attendees" style="background:linear-gradient(#8aa56e,#4d5a3e)"></span><div><b>Confrence Schedule</b><span>Lorem ipsum dolor amet laboris consectetur adipisicing elit,</span></div></div>
      <div class="news"><span class="thumb" role="img" aria-label="Orange flowers" style="background:linear-gradient(#f08a2a,#c44a12)"></span><div><b>General Information</b><span>Lorem ipsum dolor amet laboris consectetur adipisicing elit,</span></div></div>
    </div>
    <div class="abs f-col" style="left:258px">
      <h4>LATEST TWEETS</h4>
      <p class="tweet">Burger Barn's goes abstract with crowd-sourced animations: <em>http://sh.rt/k4Ra9Qe</em></p>
      <div class="time"><svg width="10" height="10" viewBox="0 0 10 10"><circle cx="5" cy="5" r="4" fill="none" stroke="#fff" stroke-width="1.3"/><path d="M5 2.5V5h2" stroke="#fff" stroke-width="1.2" fill="none"/></svg>34 mins ago</div>
      <p class="tweet">"CSV to PressKit Import" useable especially for directory presskit theme <em>http://sh.rt/Wm2pLx7</em> <em>#presskit #plugin</em></p>
      <div class="time"><svg width="10" height="10" viewBox="0 0 10 10"><circle cx="5" cy="5" r="4" fill="none" stroke="#fff" stroke-width="1.3"/><path d="M5 2.5V5h2" stroke="#fff" stroke-width="1.2" fill="none"/></svg>1 hour ago</div>
      <div class="tline"></div>
    </div>
    <div class="abs f-col" style="left:422px">
      <h4>POPULAR</h4>
      <ul class="popular"><li>Inspection FAQs</li><li>Common Venting of Gas</li><li>Becoming a Member</li><li>Education / CECs</li><li>Affiliate Directory</li><li>Lorem Lipsum</li></ul>
    </div>
    <div class="abs f-col" style="left:559px">
      <h4>GALLERY</h4>
      <div class="fg" role="img" aria-label="Grid of nine event and night-time photos">
        <div style="background:#2b3550"></div><div style="background:linear-gradient(90deg,#e8e8e8,#2a3fa0)"></div><div style="background:#3a2218"></div>
        <div style="background:linear-gradient(#d9a070,#6a4a30)"></div><div style="background:radial-gradient(#d07a3a,#2a1a10)"></div><div style="background:linear-gradient(#8a8a4a,#c48a5a)"></div>
        <div style="background:radial-gradient(#7a5a2a,#1c1410)"></div><div style="background:#3a3f4a"></div><div style="background:#4a3a30"></div>
      </div>
    </div>
    <div class="abs footbar">© 2012 Copyright by <b>Real Estate</b> &nbsp; All rights reserved.</div>
  </footer>
</main>
</body>
</html>
```